Lantern Advisory Business Cards

We need a new layout for our business cards. We have a logo already. But we might be interested in only using the Lantern portion of the logo. It has been uploaded.

We would like cards that are not overly busy. Clean. Modern. Perhaps a gray color for one side.

On the back, we would like to have the lantern part of the logo and "Take the Leap, we've got you!"

Our business provides medics and safety training for corporate clients. Our website is www.lanternadvisoryllc.example.

Industry/Entity Type

Business

Contact Information for Business Card

We want include name, email address, cell phone, main line number, and website URL on the front. Use the following as an example: Marla Tobin, marla@lanternadvisoryllc.example, 402.318.7264 (cell), 402.947.315, and www.lanternadvisoryllc.example.

Font styles to use
Serif
Sans Serif

Requirements
Must have
• All required information. Back side logo with "Take the leap, we will catch you!"
Nice to have
• If possible, we would like to consider creating a card in a non-standard shape. Perhaps, the shape of a lantern. Just interested in understanding the option.

```html
<!DOCTYPE html>
<html lang="en">
<head>
<meta charset="utf-8">
<title>Lantern Advisory – Business Cards</title>
<link rel="stylesheet" href="https://fonts.googleapis.com/css2?family=Cormorant+SC:wght@500&family=Open+Sans:wght@400;600&display=swap">
<style>
  :root {
    --page-bg: #ffffff;
    --ring-dark: #1e1e1e;
    --ring-light-top: #ececec;
    --ring-light-bottom: #363636;
    --brand-ink: #2f2f2f;
    --brand-dot: #2b5d9c;
    --text-dark: #141414;
    --text-body: #2a2a2a;
    --icon-fill: #b4b4b4;
  }
  html, body {
    margin: 0;
    padding: 0;
    overflow: hidden;
    background: var(--page-bg);
  }
  .canvas {
    position: relative;
    width: 1200px;
    height: 691px;
    background: var(--page-bg);
    overflow: hidden;
  }
  .card-art {
    position: absolute;
    inset: 0;
    width: 1200px;
    height: 691px;
  }
  .ring-dark { fill: var(--ring-dark); }
  .ring-grad-top { stop-color: var(--ring-light-top); }
  .ring-grad-bottom { stop-color: var(--ring-light-bottom); }

  .brand {
    position: absolute;
    left: 195px;
    top: 288px;
    width: 220px;
    text-align: center;
  }
  .brand-dot {
    display: block;
    width: 20px;
    height: 20px;
    margin: 0 auto 7px;
    border-radius: 50%;
    background: var(--brand-dot);
  }
  .brand-name {
    margin: 0;
    font-family: "Cormorant SC", Georgia, serif;
    font-weight: 500;
    font-size: 17px;
    line-height: 20px;
    letter-spacing: 0.2px;
    color: var(--brand-ink);
    white-space: nowrap;
  }
  .brand-tagline {
    margin: 3px 0 0;
    font-family: "Open Sans", Arial, sans-serif;
    font-weight: 400;
    font-size: 5px;
    line-height: 7px;
    letter-spacing: 1.2px;
    color: var(--brand-ink);
    white-space: nowrap;
  }

  .contact {
    position: absolute;
    left: 758px;
    top: 298px;
    font-family: "Open Sans", Arial, sans-serif;
    color: var(--text-body);
  }
  .contact-name {
    margin: 0 0 11px 22px;
    font-size: 18px;
    font-weight: 600;
    color: var(--text-dark);
  }
  .contact-list {
    list-style: none;
    margin: 0;
    padding: 0;
  }
  .contact-item {
    display: flex;
    align-items: flex-start;
    gap: 8px;
    font-size: 8.5px;
    line-height: 11px;
    margin-bottom: 8px;
  }
  .contact-icon {
    flex: none;
    width: 14px;
    height: 14px;
  }
  .contact-icon circle { fill: var(--icon-fill); }
  .contact-icon path { fill: none; stroke: #ffffff; stroke-width: 1.1; }
</style>
</head>
<body>
<main class="canvas">
  <svg class="card-art" viewBox="0 0 1200 691" xmlns="http://www.w3.org/2000/svg">
    <defs>
      <linearGradient id="ring-fade" x1="0" y1="0" x2="0" y2="1">
        <stop class="ring-grad-top" offset="0"/>
        <stop class="ring-grad-bottom" offset="1"/>
      </linearGradient>
    </defs>
    <path class="ring-dark" fill-rule="evenodd" role="img"
      aria-label="Ring of skydiver silhouettes holding hands in formation"
      d="M91 341a230 216 0 1 0 460 0a230 216 0 1 0 -460 0Z
         M189 338a116 90 0 1 1 232 0a116 90 0 1 1 -232 0Z"/>
    <path fill="url(#ring-fade)" fill-rule="evenodd" role="img"
      aria-label="Ring of skydiver silhouettes fading from light grey to dark grey"
      d="M613 351a238 220 0 1 0 476 0a238 220 0 1 0 -476 0Z
         M747 353a108 83 0 1 1 216 0a108 83 0 1 1 -216 0Z"/>
  </svg>

  <section class="brand" aria-label="Card back">
    <span class="brand-dot"></span>
    <p class="brand-name">LANTERN ADVISORY</p>
    <p class="brand-tagline">TAKE THE LEAP, WE WILL CATCH YOU!</p>
  </section>

  <section class="contact" aria-label="Card front">
    <h1 class="contact-name">Marla Tobin</h1>
    <ul class="contact-list">
      <li class="contact-item">
        <svg class="contact-icon" viewBox="0 0 14 14"><circle cx="7" cy="7" r="7"/><path d="M4 5h6v4.5H4zM4 5l3 2.4L10 5"/></svg>
        <span>marla@lanternadvisoryllc.example</span>
      </li>
      <li class="contact-item">
        <svg class="contact-icon" viewBox="0 0 14 14"><circle cx="7" cy="7" r="7"/><path d="M5 3.8l1 2-1 .8a5 5 0 0 0 2.4 2.4l.8-1 2 1-.5 1.3A6 6 0 0 1 3.7 4.3z"/></svg>
        <span>402.318.7264 (cell)<br>402.947.315</span>
      </li>
      <li class="contact-item">
        <svg class="contact-icon" viewBox="0 0 14 14"><circle cx="7" cy="7" r="7"/><path d="M7 3.5a3.5 3.5 0 1 0 0 7a3.5 3.5 0 1 0 0-7M3.5 7h7M7 3.5c-1.6 2-1.6 5 0 7M7 3.5c1.6 2 1.6 5 0 7"/></svg>
        <span>www.lanternadvisoryllc.example</span>
      </li>
    </ul>
  </section>
</main>
</body>
</html>
```